The Maplewood Learning House Web Page

We need a web design for our Day Care Center based in Brandon, Florida. We are targeting child care and educational services to middle class parents, specially the mother. We would like to see designs that matches attached logo mark. The final design should communicate higher standards for day care and educational services.

Middle class parents in the State of Florida

```html
<!DOCTYPE html>
<html lang="en">
<head>
<meta charset="utf-8">
<title>The Maplewood Learning House</title>
<link href="https://fonts.googleapis.com/css2?family=Raleway:wght@400;500;600&family=Arimo:ital,wght@0,400;0,700;1,400&family=PT+Serif&display=swap" rel="stylesheet">
<style>
:root{
  --yellow:#fdbd32;
  --navy:#0f2744;
  --text:#7a7a7a;
  --dark:#1c2a3a;
  --line:#e2e2e2;
  --white:#ffffff;
}
*{margin:0;padding:0;box-sizing:border-box}
html,body{width:776px;height:1200px;overflow:hidden;background:var(--white)}
body{position:relative;font-family:Arimo,Arial,sans-serif;color:var(--text)}
.abs{position:absolute}
.topbar{left:0;top:0;width:776px;height:52px;background:var(--yellow)}
.brand{left:70px;top:14px;display:flex;align-items:center;gap:8px}
.brand-dot{width:20px;height:20px;border-radius:50%;background:var(--navy)}
.brand-name{font-family:Raleway,sans-serif;font-weight:600;font-size:16px;color:var(--navy)}
.phone{right:166px;top:18px;font-family:Raleway,sans-serif;font-size:13px;line-height:16px;color:var(--white);white-space:nowrap;text-align:right}
.phone b{font-weight:500;color:var(--navy);margin-left:6px;letter-spacing:.4px}
.social{left:620px;top:15px;display:flex;gap:3px}
.social span{width:20px;height:20px;border-radius:50%;background:var(--white)}
.social span:nth-child(2){background:var(--navy)}
.navbar{left:0;top:52px;width:776px;height:32px;background:var(--navy)}
.nav{right:64px;top:52px;height:32px;display:flex;align-items:center;gap:16px;list-style:none;font-size:9.6px;color:var(--white)}
.nav .active{color:var(--yellow)}
.hero{left:0;top:84px;width:776px;height:334px;background:linear-gradient(100deg,#c6776a 0%,#e9b49d 30%,#d89c82 55%,#8a5a45 75%,#6d7fb8 100%)}
.tagline{left:65px;top:274px;width:326px;height:58px;background:rgba(255,255,255,.55)}
.tag-a{left:70px;top:285px;height:33px;padding:0 8px;background:var(--white);font-family:Raleway,sans-serif;font-size:25px;line-height:33px;color:var(--yellow)}
.tag-b{left:246px;top:285px;font-family:Raleway,sans-serif;font-weight:500;font-size:25px;line-height:33px;color:var(--navy)}
.sidebar{left:65px;top:371px;width:223px;height:513px;background:var(--white);box-shadow:0 0 3px rgba(0,0,0,.2)}
.side-head{height:32px;background:var(--navy);border-bottom:3px solid var(--yellow);display:flex;align-items:center;padding-left:13px;gap:9px;color:var(--white)}
.side-head.news{font-family:Raleway,sans-serif;font-size:16.5px}
.side-head.mission{font-family:"PT Serif",serif;font-size:15px;margin-top:15px}
.news-list{list-style:none;padding:11px 12px 0 12px;font-size:9.3px;line-height:13px}
.news-list li{position:relative;padding-left:11px;margin-bottom:8.5px}
.news-list li::before{content:"";position:absolute;left:1px;top:4px;width:4px;height:4px;border-radius:50%;background:var(--yellow)}
.quote{padding:20px 14px 0 13px;font-size:7.7px;line-height:13px;color:#222}
.cite{display:flex;justify-content:center;align-items:center;gap:14px;margin-top:14px;font-size:7.4px;text-align:center;color:#555}
.cite strong{display:block;margin-top:6px;color:#444}
.avatar{width:26px;height:26px;border-radius:50%;background:linear-gradient(#c9a48c,#5b6a7a);border:2px solid #ddd}
h2{font-family:Raleway,sans-serif;font-weight:500;font-size:16px;color:var(--dark);white-space:nowrap}
.welcome-title{left:306px;top:435px}
.welcome-img{left:306px;top:468px;width:152px;height:98px;border:1px solid var(--line);padding:4px;background:var(--white)}
.welcome-img div{width:100%;height:100%;background:linear-gradient(90deg,#d89aa5,#7ea4c8 50%,#c9b48f)}
.welcome-text{left:466px;top:472px;width:240px;font-size:10px;line-height:13px}
.welcome-text p{margin-bottom:13px}
.more{font-size:9.4px;color:var(--dark)}
.features-title{left:304px;top:608px}
.features-rule{left:302px;top:634px;width:392px;height:1px;background:var(--line)}
.feature{left:318px;width:386px;display:flex;gap:16px}
.feature .ic{flex:none;width:42px;height:42px;border-radius:50%;border:2px solid var(--yellow);background:#f4f4f4;display:flex;align-items:center;justify-content:center;margin-top:2px}
.feature h3{font-family:Raleway,sans-serif;font-weight:500;font-size:10.5px;color:var(--dark);margin-bottom:6px}
.feature p{font-size:10px;line-height:13px}
.divider{left:324px;width:370px;border-top:1px dashed #d6d6d6}
.staff{left:0;top:933px;width:776px;height:233px;background:var(--yellow);text-align:center}
.staff h2{margin-top:24px;font-size:16px}
.staff-intro{width:530px;margin:4px auto 0;font-size:9.6px;line-height:13px;color:var(--white)}
.member{position:absolute;width:170px;text-align:center;color:var(--dark)}
.member .ph{width:76px;height:76px;margin:0 auto;border-radius:50%;border:3px solid var(--white)}
.member .nm{margin-top:8px;font-size:11px}
.member .rl{margin-top:4px;font-size:8px;font-style:italic}
.footer{left:0;top:1166px;width:776px;height:34px;background:var(--navy);color:var(--white);font-size:8.6px;text-align:center;line-height:34px}
</style>
</head>
<body>
<div class="abs topbar"></div>
<div class="abs brand"><span class="brand-dot"></span><span class="brand-name">The Maplewood Learning House</span></div>
<div class="abs phone">Call Us Toll On <b>+1 813 555 0147</b></div>
<div class="abs social"><span></span><span></span><span></span><span></span></div>
<div class="abs navbar"></div>
<ul class="abs nav">
  <li class="active">HOME</li><li>ADDISSIONS</li><li>PHILOSOPHY</li><li>PROGRAMS</li><li>SERVICES</li><li>CAMPUSES</li><li>FRANCHISES</li>
</ul>

<div class="abs hero" role="img" aria-label="Photo of a smiling mother and young daughter in a bright classroom"></div>
<div class="abs tagline"></div>
<div class="abs tag-a">EVERY CHILD</div>
<div class="abs tag-b">IS SPECIAL</div>

<aside class="abs sidebar">
  <div class="side-head news">
    <svg width="19" height="18" viewBox="0 0 19 18"><rect x="1" y="3" width="17" height="14" rx="1" fill="none" stroke="#fff" stroke-width="1.5"/><rect x="1" y="3" width="17" height="4" fill="#fff"/><g fill="#fff"><rect x="4" y="9" width="2.5" height="2"/><rect x="8.3" y="9" width="2.5" height="2"/><rect x="12.6" y="9" width="2.5" height="2"/><rect x="4" y="12.5" width="2.5" height="2"/><rect x="8.3" y="12.5" width="2.5" height="2"/></g><rect x="5" y="1" width="1.5" height="4" fill="#fff"/><rect x="12.5" y="1" width="1.5" height="4" fill="#fff"/></svg>
    News &amp; Events
  </div>
  <ul class="news-list">
    <li>Praesent arcu gravida vehicula est node maecenas loareet morbi a dosis luctus.</li>
    <li>Praesent arcu gravida vehicula est node maecenas loareet morbi a dosis luctus. eget lacinia eleifend praesent.</li>
    <li>Praesent arcu gravida vehicula est node maecenas loareet morbi a dosis luctus. eget lacinia eleifend praesent.</li>
    <li>maecenas loareet morbi a dosis luctus. eget lacinia eleifend praesent.</li>
    <li>Praesent arcu gravida vehicula est node maecenas loareet morbi a dosis luctus. eget lacinia eleifend praesent.</li>
    <li>maecenas loareet morbi a dosis luctus. eget lacinia eleifend praesent.</li>
  </ul>
  <div class="side-head mission">
    <svg width="19" height="19" viewBox="0 0 19 19"><circle cx="9.5" cy="9.5" r="8.5" fill="none" stroke="#fff" stroke-width="1.5"/><path d="M6 12c0-3 1-4.5 3-5.5M10 12c0-3 1-4.5 3-5.5" stroke="#fff" stroke-width="2" fill="none"/></svg>
    Mission Statement
  </div>
  <p class="quote">“Ipsum is simply dummy text of the printing and typesetting industry. Lorem Ipsum has been the industry's standard dummy text ever since the 1500s, when an unknown printer took a galley of type and scrambled it to make a type specimen book.”</p>
  <div class="cite">
    <div>-EMEA Private Equity client<strong>Emerging market capabilities</strong></div>
    <div class="avatar" role="img" aria-label="Portrait of the quoted client"></div>
  </div>
</aside>

<h2 class="abs welcome-title">WELCOME TO THE MAPLEWOOD LEARNING HOUSE !</h2>
<div class="abs welcome-img"><div role="img" aria-label="Photo of two young children playing with toys at a classroom table"></div></div>
<div class="abs welcome-text">
  <p>Praesent arcu gravida vehicula est node maecenas loareet morbi a dosis luctus.</p>
  <p>Urna eget lacinia eleifend praesent luctus a arcu quis facilisis venenatis aenean interdum.Praesent arcu gravida vehicula est node maecenas loareet morbi a dosis luctus.</p>
  <div class="more">Read more ››</div>
</div>

<h2 class="abs features-title">FEATURES OF THE MAPLEWOOD LEARNING HOUSE !</h2>
<div class="abs features-rule"></div>

<div class="abs feature" style="top:649px">
  <div class="ic"><svg width="16" height="16" viewBox="0 0 16 16"><rect x="1" y="2" width="14" height="13" fill="none" stroke="#fdbd32" stroke-width="1.4"/><rect x="1" y="2" width="14" height="3.5" fill="#fdbd32"/><path d="M4 9h8M4 12h8" stroke="#fdbd32"/></svg></div>
  <div><h3>HOME SCHOOLSUPPORT</h3><p>Urna eget lacinia eleifend praesent luctus a arcu quis facilisis venenatis aenean interdum.Praesent arcu gravida vehicula est node maecenas loareet morbi a dosis luctus.</p></div>
</div>
<div class="abs divider" style="top:718px"></div>
<div class="abs feature" style="top:728px">
  <div class="ic"><svg width="18" height="16" viewBox="0 0 18 16"><path d="M2 6h3l8-4v12l-8-4H2z" fill="#fdbd32"/><path d="M4 10l1 5h2l-1-5" fill="#fdbd32"/><path d="M15 6v4" stroke="#fdbd32" stroke-width="1.5"/></svg></div>
  <div><h3>HOME SCHOOLSUPPORT</h3><p>Urna eget lacinia eleifend praesent luctus a arcu quis facilisis venenatis aenean interdum.Praesent arcu gravida vehicula est node maecenas loareet morbi a dosis luctus.</p></div>
</div>
<div class="abs divider" style="top:801px"></div>
<div class="abs feature" style="top:818px">
  <div class="ic"><svg width="18" height="16" viewBox="0 0 18 16"><rect x="1" y="2" width="11" height="8" fill="none" stroke="#fdbd32" stroke-width="1.4"/><path d="M3 8l2-2 2 1 3-3" stroke="#fdbd32" fill="none"/><circle cx="14" cy="5" r="1.8" fill="#fdbd32"/><path d="M12.5 8h3v7h-3z" fill="#fdbd32"/></svg></div>
  <div><h3>HOME SCHOOLSUPPORT</h3><p>Urna eget lacinia eleifend praesent luctus a arcu quis facilisis venenatis aenean interdum.Praesent arcu gravida vehicula est node maecenas loareet morbi a dosis luctus.</p></div>
</div>
<div class="abs more" style="left:377px;top:894px">Read more ››</div>

<section class="abs staff">
  <h2>OUR STAFF</h2>
  <p class="staff-intro">Praesent arcu gravida vehicula est node maecenas loareet morbi a dosis luctus. Urna eget lacinia eleifend praesent luctus a arcu quis facilisis venenatis aenean interdum.</p>
  <div class="member" style="left:121px;top:97px">
    <div class="ph" role="img" aria-label="Portrait of staff member Laura Benton" style="background:linear-gradient(#4a3a30,#e8c7b2)"></div>
    <div class="nm">Laura Benton</div><div class="rl">Sed diam nonummy nibh eusismod</div>
  </div>
  <div class="member" style="left:281px;top:99px">
    <div class="ph" role="img" aria-label="Portrait of staff member Nina Carrow" style="background:linear-gradient(#8a5a34,#e6c0a0)"></div>
    <div class="nm">Nina Carrow</div><div class="rl">diam nonummy nibh eusismod tinc</div>
  </div>
  <div class="member" style="left:455px;top:97px">
    <div class="ph" role="img" aria-label="Portrait of staff member Dana Whitlow" style="background:linear-gradient(#2b1d16,#8a5a40)"></div>
    <div class="nm">Dana Whitlow</div><div class="rl">nonummy nibh eusismod tincidunt ut</div>
  </div>
</section>

<footer class="abs footer">Copyright © 2015 The Maplewood Learning House. Powered by Pagecraft and Brightwork Studio</footer>
</body>
</html>
```